Create a Brochure Design for Brantley Homecare

Brantley Homecare is a subsidiary of the Brantley Care Group. This brochure is specifically for the Brantley Homecare company and brand. Create a 3 panel, A4, front and back, tri-fold brochure. This brochure will be a way to introduce our Homecare services to the community, prospective clients, and various referral partners. The brochure must be eye catching, unique in its deliverables and demonstrate both attention to detail and comfort. Our organization is sophisticated and built around warmth, care and individualized personal attention. The most important aspect of this design is to focus on creating a nurturing, warm, and inviting feel where you would want to have a Nurse or Nurse’s Aide in your own home or a loved one’s home.

I am open to the creativity of the designer to develop something based on the above criteria; however I would like the design to work well with the existing collateral material. What I mean by that is that while I want everything to have its own personality and stand out as its own brand representative, I still need to be able to tell that the overall design concept stays stylistically inside of the same ‘family’ of existing designed material. Because of this, below I would like for the designer to pull inspiration from the link to our website (Located below) as well as from the attachment of our recently refreshed business cards (Attached). This should allow each design to be unique and creative, while still staying inside of a framework and the feel/style that I am looking for.

Finally, I want all the designers to understand that this brochure design is for a private, in home, healthcare company where we are responsible for providing personalized care for a culturally and ethnically diverse make-up clientele of all ages. The photos that are used must represent an image of warmth, care, and a positive interaction between client and caregiver.

Look under the Brantley Homecare tab at www.brantleycaregroup-example.net

Industry/Entity Type

Healthcare

Requirements
Must have
• • The Brantley Homecare company logo must be included.

```html
<!DOCTYPE html>
<html lang="en">
<head>
<meta charset="utf-8">
<title>Brantley Homecare – Tri-fold Brochure</title>
<link rel="stylesheet" href="https://fonts.googleapis.com/css2?family=Open+Sans:wght@400;600;700&display=swap">
<style>
  :root {
    --backdrop: #b9b9b9;
    --paper: #ffffff;
    --teal-deep: #287471;
    --teal-soft: #5f9c99;
    --teal-brand: #1e6a5f;
    --salmon: #f0937a;
    --salmon-light: #f6b9a7;
    --text-light: #e6f1f0;
    --text-muted: #b9d6d4;
  }
  * { box-sizing: border-box; margin: 0; padding: 0; }
  html, body { width: 1200px; height: 863px; overflow: hidden; }
  body {
    background: var(--backdrop);
    font-family: "Open Sans", Arial, sans-serif;
    position: relative;
  }

  /* Inside spread */
  .inside-spread {
    position: absolute; left: 100px; top: 176px;
    width: 720px; height: 510px;
    background: var(--paper);
    display: grid; grid-template-columns: repeat(3, 240px);
  }
  .panel { position: relative; height: 510px; }
  .panel-header {
    height: 90px; background: var(--paper);
    border-top: 3px solid var(--salmon-light);
    border-bottom: 3px solid var(--salmon);
    position: relative;
  }
  .spread-logo {
    position: absolute; left: 70px; top: 24px;
    display: flex; flex-direction: column; align-items: center; gap: 5px;
  }
  .logo-mark { width: 18px; height: 18px; background: var(--salmon); }
  .logo-name { color: var(--teal-brand); font-weight: 600; font-size: 15px; white-space: nowrap; }
  .tagline {
    position: absolute; left: 22px; top: 28px; width: 200px;
    color: var(--teal-soft); font-size: 9px; font-style: normal; line-height: 1.4;
  }
  .photo { height: 157px; position: relative; border-bottom: 3px solid #e4e4e4; }
  .photo-companionship { background: linear-gradient(120deg, #c9c3bd, #e8e0da 55%, #f3efec); }
  .photo-hands { background: linear-gradient(120deg, #d7c8d6, #e9d8cf 50%, #cbbfd4); }
  .photo-visit { background: linear-gradient(120deg, #3e5a8c, #b9a7a6 50%, #c7c2c8); }
  .badge {
    position: absolute; right: 14px; bottom: 12px;
    width: 46px; height: 46px; border-radius: 50%;
    background: var(--salmon); color: #fff;
    font-size: 7px; font-weight: 600; line-height: 1.2;
    display: flex; align-items: center; justify-content: center; text-align: center;
  }
  .panel-body { height: 260px; padding: 22px 20px; color: var(--text-light); }
  .body-deep { background: var(--teal-deep); }
  .body-soft { background: var(--teal-soft); }
  .panel-body h2 { font-size: 13px; font-weight: 700; line-height: 1.3; color: #fff; margin-bottom: 10px; }
  .panel-body p { font-size: 8px; line-height: 1.55; margin-bottom: 10px; }
  .panel-body p.secondary { color: var(--text-muted); font-weight: 400; }

  /* Front cover */
  .front-cover {
    position: absolute; left: 860px; top: 176px;
    width: 240px; height: 510px; background: var(--paper);
  }
  .cover-header {
    height: 150px;
    border-top: 7px solid var(--salmon);
    border-bottom: 3px solid var(--salmon);
    display: flex; flex-direction: column; align-items: center; justify-content: center; gap: 10px;
  }
  .cover-header .logo-mark { width: 30px; height: 30px; }
  .cover-header .logo-name { font-size: 21px; }
  .cover-photo {
    height: 360px;
    background: linear-gradient(115deg, #eef1f4 0%, #cfdbe6 35%, #c79a86 62%, #9fc1df 100%);
  }
</style>
</head>
<body>

<section class="inside-spread">
  <div class="panel">
    <div class="panel-header">
      <div class="spread-logo">
        <span class="logo-mark"></span>
        <span class="logo-name">Brantley Homecare</span>
      </div>
    </div>
    <div class="photo photo-companionship" role="img" aria-label="Caregiver smiling and talking with an elderly man">
      <span class="badge">Home<br>Care</span>
    </div>
    <div class="panel-body body-deep">
      <h2>Lorem ipsum dolor sit amet at nostrum definitiones</h2>
      <p>Ponderum periculis moderatius ei per. Te eos mundi accusam adolescens, mei ne regione, eum utinam option sed. Et usu posse euismod signiferumque. Tempor hendrerit aliquando ne dolor semper timeam his.</p>
      <p class="secondary">Nulla facilisi morbi tempus iaculis urna id volutpat lacus laoreet non curabitur gravida arcu ac tortor.</p>
    </div>
  </div>

  <div class="panel">
    <div class="panel-header"></div>
    <div class="photo photo-hands" role="img" aria-label="Caregiver gently holding an elderly person's hands">
      <span class="badge">Kind<br>Hands</span>
    </div>
    <div class="panel-body body-soft">
      <h2>Lorem ipsum dolor sit amet at nostrum definitiones</h2>
      <p>Ponderum periculis moderatius ei per. Te eos mundi accusam adolescens, mei ne regione, eum utinam option sed. Et usu posse euismod signiferumque. Tempor hendrerit aliquando ne dolor semper timeam his.</p>
      <p class="secondary">Nulla facilisi morbi tempus iaculis urna id volutpat lacus laoreet non curabitur gravida arcu ac tortor.</p>
    </div>
  </div>

  <div class="panel">
    <div class="panel-header">
      <p class="tagline">Because you deserve care at home,<br>every single day</p>
    </div>
    <div class="photo photo-visit" role="img" aria-label="Nurse sitting with an elderly woman at home">
      <span class="badge">Daily<br>Support</span>
    </div>
    <div class="panel-body body-deep">
      <h2>Lorem ipsum dolor sit amet at nostrum definitiones</h2>
      <p>Ponderum periculis moderatius ei per. Te eos mundi accusam adolescens, mei ne regione, eum utinam option sed. Et usu posse euismod signiferumque. Tempor hendrerit aliquando ne dolor semper timeam his.</p>
      <p class="secondary">Nulla facilisi morbi tempus iaculis urna id volutpat lacus laoreet non curabitur gravida arcu ac tortor.</p>
    </div>
  </div>
</section>

<section class="front-cover">
  <div class="cover-header">
    <span class="logo-mark"></span>
    <span class="logo-name">Brantley Homecare</span>
  </div>
  <div class="cover-photo" role="img" aria-label="Smiling nurse beside a smiling elderly man"></div>
</section>

</body>
</html>
```